I have just launched a labour hire company and lookingfor a fresh vibrant website design

I need a landing page, a description of our services and capability, as well as an enquiries link, and register candidates link. My company is called Halvora recruitment and we supply labourers, excavator operators, and machine operators to the Civil and railway industries. I would like to stick to our logo theme and colours of Bright green, although I want a brighter green please than what I have. I have attached Images I like as well plaese. I do need a much bigger website eventually.

```html
<!DOCTYPE html>
<html lang="en">
<head>
<meta charset="utf-8">
<title>Halvora Recruitment</title>
<link href="https://fonts.googleapis.com/css2?family=Poppins:ital,wght@0,400;0,500;0,600;0,700;0,800;1,400&display=swap" rel="stylesheet">
<style>
:root{
  --green:#2db34a;
  --green-soft:#b8e6c2;
  --ink:#111111;
  --grey:#666666;
  --pale:#f3f3f3;
  --lilac:#f3f3f8;
  --footer:#000000;
  --white:#ffffff;
}
*{box-sizing:border-box;margin:0;padding:0}
html,body{width:1200px;height:4677px;overflow:hidden}
body{font-family:'Poppins',sans-serif;color:var(--ink);background:var(--white);position:relative}
.abs{position:absolute}
.green{color:var(--green)}
.btn{position:absolute;display:flex;align-items:center;justify-content:center;border:2px solid var(--green);color:var(--grey);font-size:14px;background:var(--white);text-transform:uppercase;letter-spacing:.2px}
.btn.solid{background:var(--green);color:var(--white)}

/* header */
.site-header{position:absolute;left:0;top:0;width:1200px;height:120px;background:var(--white)}
.brand{position:absolute;left:42px;top:38px;display:flex;align-items:center;gap:12px}
.brand-mark{width:40px;height:40px;background:var(--green)}
.brand-name{font-weight:600;font-size:22px;line-height:1;color:var(--ink);text-transform:uppercase}
.brand-name small{display:block;font-size:10px;margin-top:4px;letter-spacing:.5px}
.nav{position:absolute;top:58px;left:396px;display:flex;font-size:14px;text-transform:uppercase}
.nav span{margin-right:22px}

/* hero */
.hero{position:absolute;left:0;top:120px;width:1200px;height:557px;background:linear-gradient(90deg,#2b2b2e 0%,#4a4c50 55%,#6b6e72 100%)}
.hero h1{position:absolute;left:42px;top:125px;font-size:60px;line-height:72px;font-weight:800;color:var(--white)}
.hero p{position:absolute;left:42px;top:297px;width:410px;font-size:17px;line-height:21px;color:var(--white)}
.hero .btn{left:43px;top:400px;width:130px;height:46px;border-color:var(--white);color:var(--green)}

/* services */
.services{position:absolute;left:0;top:677px;width:1200px;height:766px;background:var(--pale)}
.sec-title{position:absolute;left:0;width:100%;text-align:center;font-size:34px;font-weight:500}
.sec-title b{font-weight:600;color:var(--green)}
.sec-sub{position:absolute;text-align:center;font-size:14px;line-height:19px;color:var(--grey)}
.card{position:absolute;top:252px;width:276px;height:454px;background:var(--white);box-shadow:0 2px 8px rgba(0,0,0,.15)}
.card .ph{height:240px}
.card h3{margin-top:10px;text-align:center;color:var(--green);font-size:22px;line-height:26px;font-weight:600}
.card p{margin:16px auto 0;width:230px;text-align:center;font-size:14px;line-height:19px;color:var(--grey)}
.card .btn{left:76px;top:408px;width:108px;height:34px;font-size:13px}
.arrow{position:absolute;top:440px;width:30px;height:30px}

/* about */
.about h2{position:absolute;left:109px;top:1540px;font-size:34px;font-weight:600}
.about p{position:absolute;left:109px;top:1608px;width:430px;font-size:16px;line-height:28px;color:var(--grey)}
.about .btn{left:107px;top:1783px;width:106px;height:36px;font-size:14px}
.divider{position:absolute;left:0;top:1966px;width:1180px;height:2px;background:#999}

/* blogs */
.blog{position:absolute;top:2249px;width:311px}
.blog .ph{height:300px}
.blog time{display:block;margin:32px 0 0 25px;font-size:13px;color:var(--grey)}
.blog h3{margin:18px 0 0 22px;font-size:17px;font-weight:600;color:var(--green)}
.blog p{margin:22px 0 0 25px;width:265px;font-size:13px;line-height:17px;color:var(--grey)}
.blog .btn{left:25px;top:492px;width:118px;height:34px;font-size:14px}

/* testimonials */
.testimonials{position:absolute;left:0;top:2833px;width:1200px;height:665px;background:var(--lilac)}
.avatar{position:absolute;border-radius:50%}
.quote{position:absolute;left:195px;top:450px;width:860px;text-align:center;font-style:italic;font-size:15px;line-height:28px;color:#888}
.qmark{font-style:normal;color:var(--green);font-weight:700;font-size:22px}
.t-name{position:absolute;left:0;width:100%;top:557px;padding-left:40px;text-align:center;font-size:26px;font-weight:600}
.t-role{position:absolute;left:0;width:100%;top:593px;padding-left:34px;text-align:center;font-size:14px;font-style:italic;color:#555}

/* enquiries */
.enquiries{position:absolute;left:0;top:3576px;width:1200px;height:684px;background:var(--green)}
.form-box{position:absolute;left:142px;top:100px;width:608px;height:470px;background:var(--white)}
.form-box h2{position:absolute;left:0;width:100%;top:28px;text-align:center;font-size:34px;font-weight:600}
.field{position:absolute;width:263px;height:52px;border:2px solid #bbb;border-radius:6px;background:#eeeeee;font-size:14px;color:#999;padding:14px 10px}
.form-box .btn{left:230px;top:390px;width:136px;height:44px;font-size:14px}
.contact{position:absolute;left:844px;color:var(--white)}
.contact h3{font-size:24px;font-weight:700}
.contact h4{font-size:18px;font-weight:600;line-height:20px}
.contact p{font-size:17px;line-height:20px}

/* footer */
.site-footer{position:absolute;left:0;top:4260px;width:1200px;height:417px;background:var(--footer);color:var(--white)}
.site-footer .brand{left:172px;top:138px}
.site-footer .brand-name{color:var(--white);font-size:30px}
.site-footer .brand-name small{font-size:13px}
.foot-about{position:absolute;left:176px;top:236px;width:320px;font-size:15px;line-height:19px}
.vline{position:absolute;top:165px;width:1px;height:110px;background:var(--green)}
.foot-head{position:absolute;font-size:14px;font-weight:500;color:var(--green);text-transform:uppercase}
.quick{position:absolute;left:620px;top:167px;font-size:15px;font-weight:600;line-height:31px}
.social{position:absolute;top:233px;width:28px;height:28px;border-radius:50%;border:2px solid var(--white)}
</style>
</head>
<body>

<header class="site-header">
  <div class="brand"><div class="brand-mark"></div><div class="brand-name">Halvora<small>Recruitment Pty Ltd</small></div></div>
  <nav class="nav">
    <span class="green">Home</span><span>|</span>
    <span>About Us</span><span>|</span>
    <span>Services</span><span>|</span>
    <span>Enquiries</span><span>|</span>
    <span>Contact</span><span>|</span>
    <span>Register Candidates</span>
  </nav>
</header>

<section class="hero" role="img" aria-label="Smiling worker in a yellow hard hat holding a clipboard in a warehouse">
  <h1>HALVORA<br>RECRUITMENT</h1>
  <p>Lorem ipsum dolor sit amet, consectetur adip-iscing elit. Vivamus lacinia odio vitae vestibu-lum vestibulum.</p>
  <a class="btn">Read More</a>
</section>

<section class="services">
  <h2 class="sec-title" style="top:84px">Our <b>Service</b></h2>
  <p class="sec-sub" style="left:270px;top:160px;width:660px">Lorem ipsum dolor sit amet, consectetur adipiscing elit. Vivamus lacinia odio vitae vestibulum vestibulum.</p>

  <svg class="arrow" style="left:54px" viewBox="0 0 30 30"><circle cx="15" cy="15" r="13" fill="none" stroke="#2db34a" stroke-width="2"/><path d="M17 9l-6 6 6 6" fill="none" stroke="#2db34a" stroke-width="2"/></svg>
  <svg class="arrow" style="left:1108px" viewBox="0 0 30 30"><circle cx="15" cy="15" r="13" fill="none" stroke="#2db34a" stroke-width="2"/><path d="M13 9l6 6-6 6" fill="none" stroke="#2db34a" stroke-width="2"/></svg>

  <article class="card" style="left:113px">
    <div class="ph" role="img" aria-label="Railway tracks on gravel ballast" style="background:linear-gradient(160deg,#8a7d6e,#5a5048)"></div>
    <h3>Rigorous<br>Selection Process</h3>
    <p>Halvora Recruitment em-ploys a meticulous selection process to identify and choose the most</p>
    <a class="btn">Read More</a>
  </article>
  <article class="card" style="left:445px">
    <div class="ph" role="img" aria-label="Two orange excavators on a construction site" style="background:linear-gradient(180deg,#a8cde0 0%,#c9dde6 55%,#8a8c86 100%)"></div>
    <h3>Compliance<br>Verification</h3>
    <p>The agency places a strong emphasis on compliance with industry regulations and standards. They verify that</p>
    <a class="btn solid">Read More</a>
  </article>
  <article class="card" style="left:777px">
    <div class="ph" role="img" aria-label="Yellow loader working in a lit tunnel" style="background:linear-gradient(160deg,#3b2e1c,#a9782e 60%,#3a2a18)"></div>
    <h3>Reference<br>Checking</h3>
    <p>Halvora Recruitment under-stands the importance of reli-able references. They conduct thorough</p>
    <a class="btn">Read More</a>
  </article>
</section>

<section class="about">
  <h2>About <span class="green">Us</span></h2>
  <p>Lorem ipsum dolor sit amet, consectetur adipiscing elit, sed do eiusmod tempor incididunt ut labore et dolore magna aliqua. Quis ipsum suspendisse ul-trices gravida. Risus commodo viverra maecenas accumsan lacus vel facilisis.</p>
  <a class="btn">Read More</a>
  <svg class="abs" style="left:644px;top:1500px" width="462" height="375" viewBox="0 0 462 375">
    <path d="M20 210 C20 120 140 110 200 170 C260 230 460 150 460 250 C460 340 330 375 230 365 C110 355 20 300 20 210Z" fill="#b8e6c2"/>
  </svg>
  <div class="abs" role="img" aria-label="Two engineers in hard hats reviewing plans on site" style="left:700px;top:1502px;width:400px;height:370px;border-radius:48% 52% 45% 55% / 50% 45% 55% 50%;background:linear-gradient(150deg,#cfd6dc,#8d8f8a 60%,#5b534a)"></div>
</section>

<div class="divider"></div>

<section class="blogs">
  <h2 class="sec-title" style="top:2068px">Recent <b>Blogs</b></h2>
  <p class="sec-sub" style="left:0;width:1200px;top:2140px">Lorem Ipsum available, but the majority have suffered alteration in some form.</p>
  <article class="blog" style="left:96px">
    <div class="ph" role="img" aria-label="Operator seated in a machine cab" style="background:linear-gradient(150deg,#c98a2a,#4e4a46)"></div>
    <time>FEBRUARY 09, 2020</time><h3>LOREM IPSUM AVAILABLE</h3>
    <p>Lorem Ipsum available, but the majo rity have suffered alteration in some words which look.</p>
    <a class="btn">Read More</a>
  </article>
  <article class="blog" style="left:438px">
    <div class="ph" role="img" aria-label="Two workers in hi-vis vests with a clipboard near machinery" style="background:linear-gradient(160deg,#d8d2c4,#e07a2c 60%,#6c6a64)"></div>
    <time>FEBRUARY 09, 2020</time><h3>LOREM IPSUM AVAILABLE</h3>
    <p>Lorem Ipsum available, but the majo rity have suffered alteration in some words which look.</p>
    <a class="btn">Read More</a>
  </article>
  <article class="blog" style="left:781px">
    <div class="ph" role="img" aria-label="Engineers overlooking a building site with cranes" style="background:linear-gradient(180deg,#dfe4e8,#a7aaa0 55%,#7b6f5c)"></div>
    <time>FEBRUARY 09, 2020</time><h3>LOREM IPSUM AVAILABLE</h3>
    <p>Lorem Ipsum available, but the majo rity have suffered alteration in some words which look.</p>
    <a class="btn">Read More</a>
  </article>
</section>

<section class="testimonials">
  <h2 class="sec-title green" style="top:80px;font-weight:600;padding-left:34px">Testimonials</h2>
  <div class="avatar" role="img" aria-label="Customer portrait" style="left:361px;top:240px;width:110px;height:110px;background:#d9d2cc"></div>
  <div class="avatar" role="img" aria-label="Featured customer portrait" style="left:524px;top:194px;width:202px;height:202px;border:3px solid var(--green);background:#9fb8a8"></div>
  <div class="avatar" role="img" aria-label="Customer portrait" style="left:776px;top:240px;width:110px;height:110px;background:#e6d6cc"></div>
  <p class="quote"><span class="qmark">&ldquo;</span> Lorem ipsum dolor sit amet, consetetur sadipscing elitr, sed diam nonumy eirmod tempor invidunt ut labore<br>et dolore magna aliquyam erat, sed diam &nbsp;magna aliquyam erat, sed<br>diam voluptua con tremum bombe.<span class="qmark">&rdquo;</span></p>
  <div class="t-name">Marla Quenton</div>
  <div class="t-role">Customer</div>
</section>

<section class="enquiries">
  <form class="form-box">
    <h2>Enquiries <span class="green">Form</span></h2>
    <div class="field" style="left:22px;top:110px">First Name</div>
    <div class="field" style="left:316px;top:110px">Last Name</div>
    <div class="field" style="left:25px;top:197px">Gender</div>
    <div class="field" style="left:319px;top:197px">Age</div>
    <div class="field" style="left:25px;top:285px">Date</div>
    <div class="field" style="left:321px;top:281px">Mobile Number</div>
    <a class="btn solid">Book Now</a>
  </form>
  <div class="contact" style="top:174px"><h3>CONTACT US</h3></div>
  <div class="contact" style="top:258px"><h4>CALL US</h4><p>0412 555 087</p></div>
  <div class="contact" style="top:343px"><h4>EMAIL US</h4><p>info@halvorarecruit.com</p></div>
  <div class="contact" style="top:447px"><h4>ADDRESS</h4><p>Address Line Dummy Here<br>Dummy Address Here</p></div>
</section>

<footer class="site-footer">
  <div class="brand"><div class="brand-mark"></div><div class="brand-name">Halvora<small>Recruitment Pty Ltd</small></div></div>
  <p class="foot-about">Lorem ipsum dolor sit amet, consecte-<br>tur adipiscing elcilisis.</p>
  <div class="vline" style="left:537px"></div>
  <div class="foot-head" style="left:615px;top:136px">Quick Link</div>
  <div class="quick">About us<br>Services<br>Enquiries<br>Register Candidates</div>
  <div class="vline" style="left:857px"></div>
  <div class="foot-head" style="left:902px;top:182px">Get Social With Me</div>
  <span class="social" aria-label="Social link" style="left:908px"></span>
  <span class="social" aria-label="Social link" style="left:953px"></span>
  <span class="social" aria-label="Social link" style="left:993px"></span>
  <span class="social" aria-label="Social link" style="left:1041px"></span>
</footer>

</body>
</html>
```